Label Fjordulin
Zielgruppe
Hunde- und Katzenhalter von Jung bis Alt
Aufgabenstellung
Es soll ein Flaschenetikett für folgendes Produkt entworfen werden:
Lachsöl aus Norwegen für Hunde und Katzen. Es handelt sich um ein Premium-Produkt. Der Name "Fjordulin" sowie einige weitere Etikettendetails wie Größe, Deklaration etc. liegen fest. Die Flaschenfarbe ist braun. Ansonsten ist die Gestaltung frei. Ein Musteretikett des Herstellers kann geliefert werden.
Das Ur-Produkt ist Krevanix-Lachsöl (www.krevanix.no), welches von uns als Privat-Label-Produkt erworben wird.

```html
<!DOCTYPE html>
<html lang="de">
<head>
<meta charset="utf-8">
<title>Fjordulin Etikett</title>
<link rel="stylesheet" href="https://fonts.googleapis.com/css2?family=Arimo:wght@400;700&display=swap">
<style>
  :root {
    --paper: #ffffff;
    --bg-top: #fffbd2;
    --bg-bottom: #d7a43c;
    --gold-light: #fff3a6;
    --gold-mid: #f7c40a;
    --gold-deep: #dcaa3a;
    --frame-red: #8e0a0a;
    --text-red: #a01010;
    --text-dark: #1a1206;
    --note-bg: #fffbc8;
    --emblem-fill: #f6ecd8;
  }
  html, body {
    margin: 0;
    padding: 0;
    width: 1031px;
    height: 1200px;
    overflow: hidden;
    background: var(--paper);
    font-family: "Arimo", Arial, sans-serif;
  }
  .label {
    position: relative;
    width: 1031px;
    height: 1200px;
  }
  .label-backing {
    position: absolute;
    left: 30px; top: 24px;
    width: 969px; height: 1148px;
    background: linear-gradient(to bottom, var(--bg-top) 0%, #fde58a 45%, var(--bg-bottom) 100%);
  }
  .label-frame {
    position: absolute;
    left: 72px; top: 60px;
    width: 880px; height: 1066px;
    border: 6px solid var(--frame-red);
    border-radius: 60px;
    background: linear-gradient(to bottom, var(--gold-light) 0%, var(--gold-mid) 45%, var(--gold-mid) 60%, var(--gold-deep) 100%);
  }
  .emblem {
    position: absolute;
    left: 326px; top: 114px;
    width: 380px; height: 380px;
    border-radius: 50%;
    border: 6px solid var(--frame-red);
    box-sizing: border-box;
    background: radial-gradient(circle, var(--gold-light) 70%, var(--gold-mid) 100%);
  }
  .emblem-art {
    position: absolute;
    left: 22px; top: 22px;
    width: 324px; height: 324px;
    border-radius: 50%;
    background: radial-gradient(circle at 50% 55%, #ffffff 40%, var(--emblem-fill) 100%);
  }
  .product-name {
    position: absolute;
    left: 0; width: 1031px;
    top: 490px;
    margin: 0;
    text-align: center;
    font-weight: 700;
    font-size: 124px;
    letter-spacing: 1px;
    color: var(--text-dark);
  }
  .product-claim {
    position: absolute;
    left: 0; width: 1031px;
    top: 662px;
    margin: 0;
    text-align: center;
    font-size: 40px;
    line-height: 56px;
    color: var(--text-red);
  }
  .benefits {
    position: absolute;
    left: 161px; top: 818px;
    width: 725px; height: 148px;
    border-radius: 20px;
    background: var(--note-bg);
    margin: 0;
    display: flex;
    align-items: center;
    justify-content: center;
    text-align: center;
    font-size: 30px;
    line-height: 43px;
    color: var(--text-red);
  }
  .expiry-label {
    position: absolute;
    left: 124px; top: 990px;
    margin: 0;
    font-size: 30px;
    color: var(--text-dark);
  }
  .expiry-field {
    position: absolute;
    left: 124px; top: 1050px;
    width: 208px; height: 50px;
    background: var(--note-bg);
  }
  .batch {
    position: absolute;
    left: 630px; top: 1030px;
    width: 310px;
    margin: 0;
    text-align: center;
    font-size: 30px;
    line-height: 43px;
    color: var(--text-dark);
  }
</style>
</head>
<body>
<main class="label">
  <div class="label-backing"></div>
  <div class="label-frame"></div>

  <div class="emblem">
    <div class="emblem-art" role="img" aria-label="Illustration: Hundekopf-Silhouette und sitzende Katze"></div>
  </div>

  <h1 class="product-name">Fjordulin</h1>

  <p class="product-claim">Original norwegisches Lachsöl<br>für Hunde und Katzen</p>

  <p class="benefits">Mit wichtigen Omega 3 und 6 Fettsäuren<br>für ein glänzendes Fell, gegen Ekzeme<br>und für ein langes Leben.</p>

  <p class="expiry-label">Haltbar bis</p>
  <div class="expiry-field"></div>

  <p class="batch">Chargennummer<br>PO324-H83</p>
</main>
</body>
</html>
```